Website for a company offering full serivce charging solutions for electric cars

The company "mero-kant" (english: "mero-edge") offering all-in-one-solutions for charging infrastructure for electric mobility.

There are four products:
1- Wallboxes for single-family homes
2- Solutions for property devloper/-management for property parking space
3- All-in-one-charging solution for municipalities/communities
4- Solutions for tourism/hotels/holiday appartments

The Website structure:
1. Main Page
2.1. Product Page Single Homes
2.2. Product Page Property Management / Parking
2.3. Product Page Municipality
2.4. Product Page Tourism
3. Contact Form / Request for information
4. Imprint / Legal

The Website should be built on Wordpress with a powerful possibility to simply add/modify specific landing pages.

We would like you to implement the website later and also maintain it if possible, but we would be able to do minor modifications by ourselfs (for A/B-Testing)

The website should be clear and simple, easy to understand.
Target group is mainly B2C without deeper knowledge of that topic.

It should suggest, that we will provide a very simple way to get the charging infrastructure done.

We need a contact form, maybe we will use Hubspot later.

Attached you will find a draft of the main page and a landing page (for 2.2) - it is just the content, please ignore the design. We would love to let you create a suitable design.
Also you will find some drafts a bit different for the same story.

I added also a few stock photos, but they don't need to be used! If you have better ideas, you are welcome!

Industry/Entity Type

Charging/Electric mobility

Number of Pages Required

2 page

Font styles to use
Sans Serif

Requirements
Must have
• Based on Wordpress, and the designer should be able to implement it on Wordpress on a later step

```html
<!DOCTYPE html>
<html lang="en">
<head>
<meta charset="utf-8">
<title>mero-kant – Making charging easy</title>
<link href="https://fonts.googleapis.com/css2?family=Montserrat:wght@400;500;600;700&display=swap" rel="stylesheet">
<style>
:root{
  --pink:#e8129f;
  --blue:#0033e8;
  --purple:#6f5fc4;
  --ink:#161b33;
  --muted:#2c2f3c;
  --label:#7f8fc4;
  --soft:#f8f8f9;
  --link:#6b6e7a;
}
*{margin:0;padding:0;box-sizing:border-box}
html,body{width:1200px;height:2459px;overflow:hidden;background:#fff}
body{position:relative;font-family:'Montserrat',sans-serif;color:var(--ink)}
.abs{position:absolute}
.brand{display:flex;align-items:center;gap:10px;font-weight:600;font-size:21px;color:var(--ink)}
.brand-dot{width:22px;height:22px;border-radius:50%;background:var(--pink)}
/* hero */
.hero{left:0;top:0;width:1200px;height:500px;background:linear-gradient(100deg,#f4f5f8 0%,#e9edf4 38%,#9fb6e6 58%,#2d5fd8 78%,#1237b8 100%)}
.hero-curve{left:0;top:0}
.nav{top:42px;right:88px;display:flex;gap:38px;font-size:12px;color:var(--muted)}
.nav a{color:inherit;text-decoration:none;padding-bottom:6px}
.nav .active{font-weight:700;color:var(--ink);border-bottom:2px solid #fff;box-shadow:0 2px 0 #fff}
.hero-title{left:86px;top:128px;font-size:36px;line-height:42px;font-weight:700}
.hero-text{left:86px;top:226px;width:370px;font-size:12.5px;line-height:21px;color:var(--muted)}
.btn{display:flex;align-items:center;justify-content:center;border-radius:20px;color:#fff;font-size:10.5px;font-weight:700;text-transform:uppercase;letter-spacing:.2px}
.btn-pink{background:var(--pink)}
.btn-purple{background:var(--purple)}
/* intro */
.eyebrow{font-size:10px;font-weight:700;color:var(--label);text-transform:uppercase}
.intro-title{left:89px;top:553px;font-size:26px;line-height:31px;font-weight:700}
.intro-sub{left:90px;top:652px;width:420px;font-size:13px;line-height:26px;color:var(--muted)}
.intro-right{left:625px;top:557px;width:480px;font-size:12.8px;line-height:21px;color:var(--muted)}
/* solutions */
.solutions{left:0;top:748px;width:1200px;height:852px;background:var(--soft)}
.sol-title{left:0;top:798px;width:1200px;text-align:center;font-size:21px;line-height:26px;font-weight:700}
.tab{top:879px;width:334px;height:52px;border-radius:26px;color:#fff;font-size:10.5px;font-weight:700;display:flex;align-items:center;justify-content:center}
.tab-private{left:88px;background:var(--pink);box-shadow:0 8px 18px rgba(232,18,159,.18)}
.tab-business{left:433px;background:var(--blue)}
.tab-muni{left:778px;background:var(--purple)}
.tab-pointer{left:248px;top:929px;width:0;height:0;border-left:7px solid transparent;border-right:7px solid transparent;border-top:8px solid var(--pink)}
.card{left:88px;top:962px;width:1025px;height:524px;background:#fff}
.card-title{left:158px;top:1008px;font-size:17.5px;font-weight:600;color:var(--pink)}
.card-sub{left:159px;top:1034px;font-size:11.5px;color:var(--muted)}
.feature{width:200px}
.feature svg{display:block;width:20px;height:20px}
.feature h3{margin-top:14px;font-size:14px;font-weight:700}
.feature p{margin-top:8px;font-size:11.3px;line-height:19.5px;color:var(--muted)}
.feature-bar{width:53px;height:3px;background:var(--pink)}
.products-link{left:92px;top:1541px;font-size:18px;font-weight:600;padding-bottom:4px;border-bottom:3px solid var(--ink)}
/* cta */
.cta{left:0;top:1600px;width:1200px;height:480px;background:linear-gradient(110deg,#4a5167 0%,#5b6277 45%,#6c7386 70%,#4d5469 100%)}
.cta-shape{left:0;top:1596px}
.cta-eyebrow{left:0;top:1760px;width:1200px;text-align:center;color:var(--label)}
.cta-title{left:0;top:1783px;width:1200px;text-align:center;color:#fff;font-size:27px;line-height:31px;font-weight:700}
.cta-text{left:0;top:1875px;width:1200px;text-align:center;color:#fff;font-size:12.5px}
/* footer */
.copyright{left:93px;top:2228px;font-size:13.5px;font-weight:500}
.foot-col{top:2180px}
.foot-col h4{display:inline-block;font-size:16px;font-weight:500;padding-bottom:4px;border-bottom:3px solid var(--pink)}
.foot-col ul{list-style:none;margin-top:18px}
.foot-col li{font-size:16px;color:var(--link);line-height:38px}
</style>
</head>
<body>

<!-- Hero -->
<div class="abs hero" role="img" aria-label="Photo of an electric vehicle charging plug inserted in a car port with glowing blue light ring"></div>
<svg class="abs hero-curve" width="1200" height="500" viewBox="0 0 1200 500">
  <path d="M0 401 C180 440 380 490 560 497 C580 498 600 498 620 497 L0 500 Z" fill="#fff"/>
  <path d="M0 401 C200 450 420 500 600 500 L0 500 Z" fill="#fff"/>
  <path d="M600 500 L1200 458 L1200 500 Z" fill="#fff"/>
  <path d="M640 496 L1200 401 L1200 458 Z" fill="var(--pink)"/>
</svg>

<div class="abs brand" style="left:88px;top:40px"><span class="brand-dot"></span>mero-kant.de</div>
<nav class="abs nav">
  <a class="active" href="#">Home</a><a href="#">Company</a><a href="#">Services</a><a href="#">Careers</a><a href="#">Contact</a>
</nav>
<h1 class="abs hero-title">Making charging easy<br>from a single source</h1>
<p class="abs hero-text">mero-kant is your partner when charging is not only supposed to be easy, but also when the implementation is to come from a single source</p>
<a class="abs btn btn-pink" style="left:86px;top:313px;width:142px;height:38px">Our Solution</a>

<!-- Intro -->
<div class="abs eyebrow" style="left:89px;top:531px">More than just charging</div>
<h2 class="abs intro-title">We offer solutions for<br>private customers, business<br>customers &amp; municipalities</h2>
<p class="abs intro-sub">who want to get a smart charging solution for e-vehicles quickly, fairly and without having to do anything themselves.</p>
<div class="abs intro-right">
  <p>From advice to installation, commissioning, billing and maintenance, you get everything from a single source with mero-kant.<br>On request, we can also rent out the charging technology and take care of direct billing with the user in the commercial sector.</p>
  <p style="margin-top:20px">For municipalities we offer the free full service and involve the municipalities in the use of the infrastructure.</p>
</div>

<!-- Solutions -->
<div class="abs solutions"></div>
<h2 class="abs sol-title">Click below to find the solution<br>tailored to your individual needs:</h2>
<div class="abs tab tab-private">AS A PRIVATE CUSTOMER</div>
<div class="abs tab tab-business">AS A BUSINESS CUSTOMER</div>
<div class="abs tab tab-muni">AS A MUNICIPALITY</div>
<div class="abs tab-pointer"></div>

<div class="abs card"></div>
<div class="abs card-title">As a Private Customer :</div>
<div class="abs card-sub">From advice to installation, commissioning, billing and</div>

<div class="abs feature" style="left:159px;top:1096px">
  <svg viewBox="0 0 20 20"><rect x="1" y="1" width="18" height="18" rx="2" fill="var(--ink)"/><path d="M4 14 L8 9 L11 12 L16 5" stroke="#fff" stroke-width="2" fill="none"/></svg>
  <h3>Analysis</h3><p>Analysis of the situation with extensive advice on the possibilities of implementation</p>
</div>
<div class="abs feature" style="left:391px;top:1096px">
  <svg viewBox="0 0 20 20"><rect x="0" y="2" width="20" height="16" rx="1" fill="var(--ink)"/><rect x="0" y="6" width="20" height="3" fill="#fff"/><rect x="3" y="12" width="6" height="2" fill="#fff"/></svg>
  <h3>Funding</h3><p>Checking and acceptance of the registration for available funding opportunities</p>
</div>
<div class="abs feature" style="left:623px;top:1096px">
  <svg viewBox="0 0 20 20"><path d="M10 1 L18 5.5 V14.5 L10 19 L2 14.5 V5.5 Z M2 5.5 L10 10 L18 5.5 M10 10 V19" stroke="var(--ink)" stroke-width="1.8" fill="none" stroke-linejoin="round"/></svg>
  <h3>Wallbox</h3><p>Selection of smart wallbox solutions, suitable for your vehicle and your needs</p>
</div>
<div class="abs feature" style="left:855px;top:1096px">
  <svg viewBox="0 0 20 20"><rect x="1" y="1" width="18" height="18" rx="2" fill="var(--ink)"/><path d="M4 14 L8 9 L11 12 L16 5" stroke="#fff" stroke-width="2" fill="none"/></svg>
  <h3>Installation</h3><p>Installation including all necessary materials and activities (breakthroughs, earthworks, etc.)</p>
</div>
<div class="abs feature-bar" style="left:159px;top:1226px"></div>
<div class="abs feature-bar" style="left:391px;top:1226px"></div>
<div class="abs feature-bar" style="left:623px;top:1226px"></div>
<div class="abs feature-bar" style="left:855px;top:1226px"></div>

<div class="abs feature" style="left:159px;top:1293px">
  <svg viewBox="0 0 20 20"><path d="M4 1 H12 L17 6 V19 H4 Z" stroke="var(--ink)" stroke-width="1.8" fill="none" stroke-linejoin="round"/><path d="M7 10 H14 M7 13 H14 M7 16 H12" stroke="var(--ink)" stroke-width="1.5"/></svg>
  <h3>Instrcution</h3><p>Commissioning and<br>instruction in charging<br>technology</p>
</div>
<div class="abs feature" style="left:391px;top:1293px">
  <svg viewBox="0 0 20 20"><path d="M3 3 L17 17 M17 3 L3 17" stroke="var(--ink)" stroke-width="3" stroke-linecap="round"/><circle cx="4" cy="4" r="3" fill="var(--ink)"/></svg>
  <h3>Maintenance</h3><p>Annual technical<br>maintenance according<br>to DGUV3</p>
</div>
<div class="abs feature" style="left:623px;top:1293px">
  <svg viewBox="0 0 20 20"><path d="M4 6 A8 8 0 1 1 3 12" stroke="var(--ink)" stroke-width="2" fill="none"/><path d="M2 2 V7 H7" stroke="var(--ink)" stroke-width="2" fill="none"/><path d="M10 6 V10 L13 12" stroke="var(--ink)" stroke-width="2" fill="none"/></svg>
  <h3>Repairs</h3><p>Repair service, taking into<br>account the applicable<br>warranty claims</p>
</div>
<div class="abs feature" style="left:855px;top:1293px">
  <svg viewBox="0 0 20 20"><rect x="1" y="1" width="18" height="18" rx="2" fill="var(--ink)"/><path d="M4 14 L8 9 L11 12 L16 5" stroke="#fff" stroke-width="2" fill="none"/></svg>
  <h3>Analysis</h3><p>Analysis of the situation with extensive advice on the possibilities of implementation</p>
</div>
<div class="abs feature-bar" style="left:159px;top:1423px"></div>
<div class="abs feature-bar" style="left:391px;top:1423px"></div>
<div class="abs feature-bar" style="left:623px;top:1423px"></div>
<div class="abs feature-bar" style="left:855px;top:1423px"></div>

<div class="abs products-link">View our products</div>

<!-- Call to action -->
<div class="abs cta" role="img" aria-label="Muted photo of a hand plugging a charging cable into an electric car"></div>
<svg class="abs cta-shape" width="1200" height="530" viewBox="0 0 1200 530">
  <path d="M0 0 L0 4 C200 50 420 84 600 84 C780 84 1000 50 1200 4 L1200 0 Z" fill="var(--soft)"/>
  <path d="M0 484 L1200 484 L1200 530 L0 530 Z" fill="#fff"/>
  <path d="M0 484 C200 500 450 522 600 522 C750 522 1000 500 1200 484 Z" fill="#f0f0f2"/>
</svg>
<div class="abs eyebrow cta-eyebrow">Lets discuss your charging needs</div>
<h2 class="abs cta-title">Interested in our products and<br>services? We'd love to hear from you</h2>
<p class="abs cta-text">who want to get a smart charging solution for e-vehicles</p>
<a class="abs btn btn-pink" style="left:427px;top:1941px;width:142px;height:38px">Contact Us</a>
<a class="abs btn btn-purple" style="left:618px;top:1941px;width:142px;height:38px">Our Services</a>

<!-- Footer -->
<div class="abs brand" style="left:91px;top:2182px"><span class="brand-dot"></span>mero-kant.de</div>
<div class="abs copyright">© Copyright name 2022</div>
<div class="abs foot-col" style="left:412px"><h4>Home</h4><ul><li>Services</li><li>Products</li><li>Projects</li><li>FAQ</li></ul></div>
<div class="abs foot-col" style="left:685px"><h4>About</h4><ul><li>AGB</li><li>Company</li><li>Contact</li><li>Careers</li></ul></div>
<div class="abs foot-col" style="left:964px"><h4>Legal</h4><ul><li>Data protection</li><li>Imprint</li><li>Parent Company</li><li>Email</li></ul></div>

</body>
</html>
```